WWW.VELTRONA.IT BUSINNES CARD

WE NEED A BUSINESS CARD . I HAVE A COMPANY IN ITALY NR 1 IN HAIR MEDICAL CARE AN HAIR REPLECEMENT . IN CARD I NEED WRITE WEB ADDRESS, MAIL , ADDRESS, TELEPHONE NUMBER , AND NAME
IN THE BACK SIDE I NEED MY DOCTOR LOGO .
MY WEB SITE IS WWW.VELTRONA.IT
Updates

Target Market(s)

CONSUMER B2C

Industry/Entity Type

Hair And Beauty

Contact Information for Business Card

I WANT A MEDICAL BUSINESS CARD.

Font styles to use
Other font styles liked:
• VERDANA

Colors
33a6d7
3176b5
85abd2
aedbee
eaf1f7
ffffff

Requirements
Must have
• I NEED MY LOGO AND LOGO OF DR VELTRONA

```html
<!DOCTYPE html>
<html lang="it">
<head>
<meta charset="utf-8">
<title>Veltrona – Business Card</title>
<link rel="stylesheet" href="https://fonts.googleapis.com/css2?family=Open+Sans:wght@400;600;700&display=swap">
<style>
  :root {
    --sky: #33a6d7;
    --ocean: #3176b5;
    --navy: #1d4f86;
    --mist: #85abd2;
    --ice: #aedbee;
    --frost: #eaf1f7;
    --paper: #ffffff;
    --ink: #2a2a2a;
    --stage: #dfe3e8;
  }
  * { box-sizing: border-box; margin: 0; padding: 0; }
  html, body {
    width: 1200px; height: 997px; overflow: hidden;
    background: var(--stage);
    font-family: "Open Sans", Verdana, sans-serif;
  }
  .card {
    position: absolute;
    width: 540px; height: 310px;
    border-radius: 14px;
    overflow: hidden;
    background: var(--paper);
    box-shadow: 0 10px 30px rgba(0,0,0,.18);
  }
  .card-bands { position: absolute; inset: 0; width: 100%; height: 100%; }

  /* Back side */
  .card-back {
    left: 40px; top: 190px;
    background: linear-gradient(160deg, var(--paper) 0%, var(--frost) 100%);
  }
  .back-brand {
    position: absolute; left: 40px; top: 158px;
    display: flex; align-items: center; gap: 14px;
  }
  .brand-square {
    width: 42px; height: 42px; border-radius: 8px; background: var(--sky);
  }
  .back-brand .brand-name {
    font-size: 52px; font-weight: 700; color: var(--ocean); line-height: 1;
  }
  .mascot-area {
    position: absolute; right: 24px; top: 14px;
    width: 140px; height: 200px; border-radius: 50% 50% 40% 40%;
    background: radial-gradient(ellipse at 50% 80%, #e7b48f 0%, #b98255 45%, rgba(185,130,85,0) 75%);
    opacity: .85;
  }

  /* Front side */
  .card-front { left: 620px; top: 470px; }
  .front-brand {
    position: absolute; left: 150px; top: 50px;
    display: flex; align-items: center; gap: 12px;
  }
  .front-brand .brand-square { width: 34px; height: 34px; border-radius: 6px; }
  .front-brand .brand-name {
    font-size: 46px; font-weight: 700; color: var(--ocean); line-height: 1;
  }
  .tagline {
    position: absolute; left: 150px; top: 104px;
    font-size: 13px; font-weight: 600; letter-spacing: .06em; color: var(--ocean);
    line-height: 18px;
  }
  .holder {
    position: absolute; right: 28px; top: 168px; text-align: right;
  }
  .holder-name { font-size: 14px; font-weight: 700; color: var(--ocean); }
  .holder-role { font-size: 12px; color: var(--ink); }
  .contacts {
    position: absolute; left: 44px; top: 200px;
    list-style: none; font-size: 13px; color: var(--ink); line-height: 24px;
  }
</style>
</head>
<body>

<section class="card card-back" aria-label="Retro del biglietto">
  <svg class="card-bands" viewBox="0 0 540 310" aria-hidden="true">
    <path d="M330 282 Q345 262 370 262 H540 V310 H0 V290 H320 Z" fill="var(--sky)"/>
    <path d="M0 298 H540 V310 H0 Z" fill="var(--ocean)"/>
  </svg>
  <div class="mascot-area" role="img" aria-label="Illustrazione della mascotte: un capello sorridente in camice da medico"></div>
  <div class="back-brand">
    <span class="brand-square"></span>
    <span class="brand-name">Veltrona</span>
  </div>
</section>

<section class="card card-front" aria-label="Fronte del biglietto">
  <svg class="card-bands" viewBox="0 0 540 310" aria-hidden="true">
    <path d="M120 196 Q300 170 470 118 Q300 178 120 200 Z" fill="var(--sky)"/>
    <path d="M0 284 H340 Q350 262 372 262 H540 V310 H0 Z" fill="var(--sky)"/>
    <path d="M0 292 H335 Q350 292 358 280 Q366 270 385 270 H540 V310 H0 Z" fill="var(--navy)"/>
    <rect x="0" y="198" width="30" height="86" fill="var(--sky)"/>
    <!-- phone -->
    <rect x="10" y="204" width="10" height="15" rx="2" fill="none" stroke="var(--paper)" stroke-width="1.6"/>
    <!-- mail -->
    <rect x="8" y="231" width="14" height="10" fill="none" stroke="var(--paper)" stroke-width="1.6"/>
    <path d="M8 231 L15 237 L22 231" fill="none" stroke="var(--paper)" stroke-width="1.4"/>
    <!-- pin -->
    <path d="M15 270 C10 264 9 261 9 259 A6 6 0 0 1 21 259 C21 261 20 264 15 270 Z" fill="var(--paper)"/>
    <circle cx="15" cy="259" r="2" fill="var(--sky)"/>
  </svg>
  <div class="front-brand">
    <span class="brand-square"></span>
    <span class="brand-name">Veltrona</span>
  </div>
  <p class="tagline">CURA E REINTEGRAZIONE DEI CAPELLI</p>
  <div class="holder">
    <p class="holder-name">Marco L. Ferretti</p>
    <p class="holder-role">Director &amp; Business Adviser</p>
  </div>
  <ul class="contacts">
    <li>555-014-2278</li>
    <li>marco@veltrona.it</li>
    <li>24/18 Riva street, Lecco</li>
  </ul>
</section>

</body>
</html>
```